OREV - Helping People with Disabilities

OREV is a nonprofit that strives to enable people with physical disabilities to live meaningful, quality lives. OREV needs a professional attractive website that:
• establishes a strong brand image
• presents Orev's services to those who need it
• raises funds from potential donors
Please see WORD DOC attached for more information about design vision.

Target Market(s)

people with disabilities

Industry/Entity Type

charity website

Number of Pages Required

2 page

Font styles to use
Sans Serif

Requirements
Must have
• 1. 2 pages means 1 design for homepage and 1 design for top of inner pages (banner ideas)
Nice to have
• please see attached design brief (WORD DOC)

```html
<!DOCTYPE html>
<html lang="en">
<head>
<meta charset="utf-8">
<title>OREV – A Good Life For Everyone</title>
<link href="https://fonts.googleapis.com/css2?family=Josefin+Sans:wght@500;600;700&family=Poppins:wght@400;500;600&display=swap" rel="stylesheet">
<style>
:root{
  --teal:#1f6e6c;
  --teal-dark:#17504f;
  --aqua:#23b9b6;
  --blue:#1a73c9;
  --ink:#1b1b1b;
  --muted:#555;
  --mint:#eafbfb;
  --white:#fff;
  --sunset-a:#f7a64a;
  --sunset-b:#c8512a;
  --sunset-c:#5a2414;
}
*{box-sizing:border-box;margin:0;padding:0}
html,body{width:1200px;height:3919px;overflow:hidden}
body{position:relative;font-family:'Poppins',sans-serif;color:var(--ink);background:var(--white)}
.abs{position:absolute}
h1,h2,h3{font-family:'Josefin Sans',sans-serif;font-weight:600}

/* hero */
.hero{left:0;top:0;width:1200px;height:647px;
  background:radial-gradient(ellipse 420px 300px at 830px 300px,#ffe7a8 0%,var(--sunset-a) 30%,var(--sunset-b) 65%,var(--sunset-c) 100%);}
.hero-ground{left:0;top:540px;width:1200px;height:107px;background:linear-gradient(180deg,rgba(40,15,5,0) 0%,#1e0c05 90%)}
.toplinks{top:18px;left:648px;display:flex;gap:44px;font-size:12.5px;font-weight:500;color:var(--white);letter-spacing:.2px}
.navbar{left:129px;top:49px;width:931px;height:57px;background:var(--white);clip-path:polygon(30px 0,100% 0,calc(100% - 30px) 100%,0 100%)}
.brand{left:196px;top:58px;height:40px;display:flex;align-items:center;gap:8px;font-family:'Josefin Sans',sans-serif;font-weight:700;font-size:22px;color:var(--teal)}
.brand i{width:12px;height:12px;background:var(--teal);display:block}
.nav{left:496px;top:68px;display:flex;gap:24px;font-size:14px;color:var(--ink)}
.nav-mark{left:508px;top:100px;width:30px;height:6px;background:var(--teal);transform:skewX(-30deg)}
.hero-title{left:176px;top:204px;font-size:60px;line-height:59px;color:var(--white);font-weight:600}
.btn{display:flex;align-items:center;justify-content:center;background:var(--aqua);color:var(--white);font-size:12.5px;position:absolute;overflow:hidden}
.btn::after{content:"";position:absolute;right:0;top:0;border-top:22px solid var(--teal-dark);border-left:22px solid transparent}
.hero-btn{left:175px;top:421px;width:246px;height:34px}
.dots{left:172px;top:551px;display:flex;gap:6px}
.dots span{width:28px;height:5px;background:rgba(255,255,255,.35);transform:skewX(-30deg)}
.dots span.on{background:var(--aqua)}

/* who */
.who-art{left:0;top:752px}
.who-title{left:651px;top:778px;font-size:42px}
.who-text{left:650px;top:850px;width:380px;font-size:13.2px;line-height:22.8px;color:#444}
.who-text a{color:var(--blue);font-weight:600}
.who-btn{left:650px;top:1150px;width:138px;height:32px}

/* offer */
.offer-title{left:0;top:1310px;width:1200px;text-align:center;font-size:42px}
.card{top:1402px;width:205px;height:344px;background:var(--white);box-shadow:0 2px 10px rgba(0,0,0,.12);clip-path:polygon(0 0,calc(100% - 14px) 0,100% 14px,100% 100%,14px 100%,0 calc(100% - 14px))}
.card-img{position:absolute;left:6px;top:6px;width:193px;height:200px;clip-path:polygon(0 0,calc(100% - 22px) 0,100% 22px,100% 100%,0 100%)}
.card h3{position:absolute;top:216px;left:0;width:100%;text-align:center;font-size:17px;line-height:20px}
.card p{position:absolute;left:12px;width:181px;text-align:center;font-size:12px;line-height:19px;color:#555;height:57px;overflow:hidden}
.card .more{position:absolute;top:308px;left:0;width:100%;text-align:center;color:var(--blue);font-size:13px;font-weight:500}

/* band */
.band{left:0;top:1843px;width:1200px;height:350px;background:var(--teal)}
.band h2{position:absolute;left:0;top:88px;width:1200px;text-align:center;color:var(--white);font-size:43px;line-height:53px}
.band-btn{left:496px;top:2073px;width:208px;height:34px;background:var(--white);color:var(--teal);font-size:12.5px}

/* news & location */
.sec-title{font-size:42px}
.news{left:176px;width:417px;height:122px;background:var(--mint);clip-path:polygon(0 0,calc(100% - 22px) 0,100% 22px,100% 100%,0 100%)}
.news-img{position:absolute;left:2px;top:2px;width:148px;height:118px;clip-path:polygon(0 0,100% 0,100% calc(100% - 20px),calc(100% - 20px) 100%,0 100%)}
.news small{position:absolute;left:166px;top:12px;font-size:10px;color:#666}
.news h4{position:absolute;left:166px;top:28px;font-size:14.5px;font-weight:500}
.news p{position:absolute;left:166px;top:54px;width:230px;font-size:11.2px;line-height:19px;color:#555}
.map-accent{left:728px;top:2468px;width:312px;height:312px;background:var(--teal);clip-path:polygon(100% 0,100% 100%,0 100%,20px 88%,calc(100% - 12px) 88%,calc(100% - 12px) 10px)}
.map{left:628px;top:2357px;width:399px;height:411px;background:linear-gradient(135deg,#eef0f3,#e4e7ea 60%,#d8eedd)}

/* contact */
.contact-photo{left:560px;top:2860px;width:640px;height:653px;background:linear-gradient(90deg,#fff 0%,#f6e7d3 20%,#e9c79c 50%,#c6926a 80%,#8a6a52 100%)}
.contact-title{left:175px;top:2926px;font-size:42px}
.field{left:175px;width:417px;background:rgba(255,255,255,.92);border:1px solid #cfcfcf;font-size:13px;color:#777;padding:0 22px;display:flex;align-items:center;justify-content:space-between}
.field.msg{align-items:flex-start;padding-top:18px}
.field svg{width:16px;height:16px;fill:#555}
.submit{left:175px;top:3383px;width:125px;height:33px;background:#1aa0e0;font-size:12.5px}
.submit::after{border-top-color:#127db2}

/* footer */
.footer{left:0;top:3513px;width:1200px;height:360px;background:var(--teal)}
.foot-brand{left:175px;top:3616px;font-family:'Josefin Sans',sans-serif;font-weight:700;font-size:46px;color:var(--white);display:flex;align-items:center;gap:10px}
.foot-brand i{display:block;width:14px;height:14px;background:var(--white)}
.foot-about{left:174px;top:3718px;width:320px;font-size:13px;line-height:23px;color:#e4f2f1}
.foot-h{font-size:17px;color:var(--white);font-weight:500;top:3587px}
.foot-links{left:570px;top:3640px;font-size:12.5px;color:var(--white);line-height:36px}
.contact-row{left:811px;display:flex;align-items:center;gap:14px;font-size:12.5px;color:var(--white);line-height:18px}
.ico{width:36px;height:36px;background:var(--white);display:flex;align-items:center;justify-content:center;flex:none}
.ico svg{width:16px;height:16px;fill:var(--teal)}
.socials{left:811px;top:3792px;display:flex;gap:12px}
.socials span{width:23px;height:23px;border-radius:50%;border:2px solid var(--white)}
.copy{left:0;top:3873px;width:1200px;height:46px;background:var(--teal-dark);color:#9fc4c2;font-size:12px;display:flex;align-items:center;justify-content:center}
.copy b{color:#f5d23a;font-weight:500;margin:0 4px}
</style>
</head>
<body>

<!-- HERO -->
<div class="abs hero" role="img" aria-label="Silhouette of a wheelchair user raising both arms against a bright sunset sky"></div>
<div class="abs hero-ground"></div>
<nav class="abs toplinks"><span>JOIN OREV</span><span>DONATE TO OREV</span><span>CONTACT US</span></nav>
<div class="abs navbar"></div>
<div class="abs brand"><i></i>OREV</div>
<nav class="abs nav"><span>About Us</span><span>Programs</span><span>Rehabilitation And Sports</span><span>Rights Realization</span></nav>
<div class="abs nav-mark"></div>
<h1 class="abs hero-title">A Good Life For<br>Everyone, Like<br>Everyone</h1>
<a class="btn hero-btn">Donate To Help Us Help Them</a>
<div class="abs dots"><span></span><span class="on"></span><span></span></div>

<!-- WHO WE ARE -->
<svg class="abs who-art" width="600" height="465" viewBox="0 752 600 465">
  <defs>
    <linearGradient id="gA" x1="0" y1="0" x2="1" y2="1"><stop offset="0" stop-color="#b9313a"/><stop offset=".6" stop-color="#d9c3ae"/><stop offset="1" stop-color="#9ec3b7"/></linearGradient>
    <linearGradient id="gB" x1="0" y1="0" x2="1" y2="1"><stop offset="0" stop-color="#2a7e7a"/><stop offset=".5" stop-color="#c8a88a"/><stop offset="1" stop-color="#e8d8c4"/></linearGradient>
  </defs>
  <g role="img" aria-label="Team mascot cheering beside a child in a wheelchair on a basketball court">
    <polygon points="5,1202 250,759 593,759 540,858 365,858 200,1202" fill="url(#gA)"/>
    <polygon points="196,1209 372,906 593,906 430,1209" fill="url(#gB)" stroke="#fff" stroke-width="5"/>
  </g>
</svg>
<h2 class="abs who-title">Who We Are</h2>
<p class="abs who-text">The Orev Association strives to enable people with physical disabilities to live meaningful and high-quality lives.<br>Since 1952, spurred by the polio virus outbreak, OREV has been providing a wide range of activities for children and adults with disabilities to enable them to live independently and integrate into society.<br>In over 30 cities across the country, we provide a wide variety of <a>programs</a> for children and adults with physical disabilities and their family members, helping to improve motor skills, build self-confidence, and create a sense of long-term ability.</p>
<a class="btn who-btn">Learn More</a>

<!-- WHAT WE OFFER -->
<h2 class="abs offer-title">What We Offer You</h2>
<div class="abs card" style="left:172px">
  <div class="card-img" role="img" aria-label="Smiling student holding a green folder" style="background:linear-gradient(160deg,#d9a43a,#7d4a2a)"></div>
  <h3>Education</h3>
  <p style="top:244px">OREV works to impart education and knowledge to people with disabilities and</p>
  <span class="more">Learn More &nbsp;→</span>
</div>
<div class="abs card" style="left:389px">
  <div class="card-img" role="img" aria-label="Table tennis match in a sports hall" style="background:linear-gradient(160deg,#3d55b8,#c94a5a)"></div>
  <h3>Sports And Rehab</h3>
  <p style="top:244px">OREV encourages people with disabilities to play sports and find new strengths in</p>
  <span class="more">Learn More &nbsp;→</span>
</div>
<div class="abs card" style="left:607px">
  <div class="card-img" role="img" aria-label="Group of participants celebrating at an event" style="background:linear-gradient(160deg,#9aa6a6,#c24a4a)"></div>
  <h3>Rights Realization</h3>
  <p style="top:244px">OREV works to impart education and knowledge to people with disabilities and</p>
  <span class="more">Learn More &nbsp;→</span>
</div>
<div class="abs card" style="left:824px">
  <div class="card-img" role="img" aria-label="Volunteers walking together on an outdoor trail" style="background:linear-gradient(180deg,#c9dbe8,#9db07a 55%,#c2a88a)"></div>
  <h3>Community<br>Infrastructure</h3>
  <p style="top:264px;height:38px">OREV works to impart education and knowledge to</p>
  <span class="more">Learn More &nbsp;→</span>
</div>

<!-- BAND -->
<section class="abs band">
  <h2>Even people with disabilities can be<br>with everyone, like everyone</h2>
</section>
<a class="btn band-btn">Don't Leave Them Behind</a>

<!-- NEWS -->
<h2 class="abs sec-title" style="left:172px;top:2282px">Our News</h2>
<h2 class="abs sec-title" style="left:639px;top:2282px">Our Location</h2>
<article class="abs news" style="top:2368px">
  <div class="news-img" role="img" aria-label="Performers on stage" style="background:linear-gradient(135deg,#3a1e1a,#a8403a)"></div>
  <small>2 Days Ago</small><h4>Lorem Ipsum is simply dummy</h4>
  <p>Lorem ipsum dolor sit amet, consectetur adipiscing elit, sed do eiusmod tempor incididunt ut labore et</p>
</article>
<article class="abs news" style="top:2507px">
  <div class="news-img" role="img" aria-label="Children playing outdoors" style="background:linear-gradient(135deg,#c8a070,#4f6f4a)"></div>
  <small>2 Days Ago</small><h4>Lorem Ipsum is simply dummy</h4>
  <p>Lorem ipsum dolor sit amet, consectetur adipiscing elit, sed do eiusmod tempor incididunt ut labore et</p>
</article>
<article class="abs news" style="top:2647px">
  <div class="news-img" role="img" aria-label="Friends in wheelchairs in a park" style="background:linear-gradient(135deg,#7a9a6a,#d8c6a8)"></div>
  <small>2 Days Ago</small><h4>Lorem Ipsum is simply dummy</h4>
  <p>Lorem ipsum dolor sit amet, consectetur adipiscing elit, sed do eiusmod tempor incididunt ut labore et</p>
</article>
<div class="abs map-accent"></div>
<div class="abs map" role="img" aria-label="Street map showing the association office location"></div>

<!-- CONTACT -->
<div class="abs contact-photo" role="img" aria-label="Woman standing with arms outstretched on a wheelchair on a sunlit beach"></div>
<h2 class="abs contact-title">Contact Us</h2>
<div class="abs field" style="top:3019px;height:56px">Enter Your Name<svg viewBox="0 0 16 16"><circle cx="8" cy="5" r="3.4"/><path d="M1.5 15c0-3.6 3-5.5 6.5-5.5s6.5 1.9 6.5 5.5z"/></svg></div>
<div class="abs field" style="top:3091px;height:55px">Enter Your Email<svg viewBox="0 0 16 16"><path d="M1 3h14v2L8 9 1 5z"/><path d="M1 6.5l7 4 7-4V13H1z"/></svg></div>
<div class="abs field" style="top:3159px;height:56px">Enter Your Phone<svg viewBox="0 0 16 16"><path d="M3.5 1l2.4 3-1.4 1.8c.9 2 2.7 3.8 4.7 4.7L11 9.1l3 2.4-1.5 2.9C7 14 2 9 1.6 3.5z"/></svg></div>
<div class="abs field msg" style="top:3231px;height:114px">Enter Your Message<svg viewBox="0 0 16 16"><path d="M2 3h7v1.5H3.5v8h8V8H13v6H2z"/><path d="M12.3 1.5l2.2 2.2-6 6H6.3V7.5z"/></svg></div>
<a class="btn submit">SUBMIT</a>

<!-- FOOTER -->
<footer class="abs footer"></footer>
<div class="abs foot-brand"><i></i>OREV</div>
<p class="abs foot-about">The Orev Association strives to enable people with physical disabilities to live meaningful and high-quality lives.</p>
<h4 class="abs foot-h" style="left:570px">Quick Links</h4>
<div class="abs foot-links">About Us<br>Programs<br>Rehabilitation And Sports<br>Rights Realization<br>Contact Us</div>
<h4 class="abs foot-h" style="left:811px">Contact Info</h4>
<div class="abs contact-row" style="top:3634px"><span class="ico"><svg viewBox="0 0 16 16"><path d="M3.5 1l2.4 3-1.4 1.8c.9 2 2.7 3.8 4.7 4.7L11 9.1l3 2.4-1.5 2.9C7 14 2 9 1.6 3.5z"/></svg></span>03-5550142</div>
<div class="abs contact-row" style="top:3682px"><span class="ico"><svg viewBox="0 0 16 16"><path d="M1 3h14v2L8 9 1 5z"/><path d="M1 6.5l7 4 7-4V13H1z"/></svg></span>hello@orev-assoc.org</div>
<div class="abs contact-row" style="top:3730px"><span class="ico"><svg viewBox="0 0 16 16"><path d="M8 1a5 5 0 0 1 5 5c0 4-5 9-5 9S3 10 3 6a5 5 0 0 1 5-5zm0 3a2 2 0 1 0 0 4 2 2 0 0 0 0-4z"/></svg></span>12 Cedar Lane PO Box<br>4410 Riverton 4951600</div>
<div class="abs socials"><span></span><span></span><span></span></div>
<div class="abs copy">Copyright © 2023 | <b>OREV</b> All Rights Reserved.</div>

</body>
</html>
```